Business Card Design job - Tyre Shop

Client wants a double sided business cards designed for a Tyre Shop.

The logo can be used in multiple ways, some examples are attached.

The reference font is:
https://www.typebarrow.com/fonts/open-sans
Others can be applied.

Color scheme should be mainly black and white, and red as a third less used color.

Contact Information for Business Card

Required Fields (Portuguese language):
- Name "Augusto Melro"
- Title "Gerente"
- Phone "253 704 862"
- Website "www.rodaslume.pt"
- Email "geral@rodaslume.pt
- Address "Rua da Fonteira N.187
5120-418 Vale Sereno, Alcova"

Font styles to use
Sans Serif

Requirements
Must have
• Corporate Logo
Nice to have
• The client would like the card to have special feature to measure the tyre tread, as shown in examples attached.
• The tread Values as Portuguese law are:
• - Ilegal - less than 1.6mm
• - change tyres - between 3mm and 1.6 mm
• - OK - above 3mm
• Card should be kept standard rectangle size 85x55mm

```html
<!DOCTYPE html>
<html lang="pt">
<head>
<meta charset="utf-8">
<title>Rodas Lume – Cartão de Visita</title>
<link href="https://fonts.googleapis.com/css2?family=Open+Sans:wght@400;600;700&display=swap" rel="stylesheet">
<style>
  :root {
    --bg: #d9dcdf;
    --card-white: #ffffff;
    --card-dark: #1f2023;
    --card-dark-2: #2a2b2f;
    --ink: #111111;
    --red: #e5141d;
    --pink: #ef6a8a;
    --grey-1: #7f8589;
    --grey-2: #a9aeb1;
  }
  * { margin: 0; padding: 0; box-sizing: border-box; }
  html, body { width: 1200px; height: 1200px; overflow: hidden; }
  body {
    background: var(--bg);
    font-family: "Open Sans", Arial, sans-serif;
    display: flex;
    flex-direction: column;
    align-items: center;
    justify-content: center;
    gap: 40px;
  }
  .card {
    position: relative;
    width: 760px;
    height: 492px;
    overflow: hidden;
    box-shadow: 0 6px 20px rgba(0,0,0,0.18);
  }

  /* Front */
  .card-front { background: var(--card-white); }
  .card-front .brand {
    position: absolute;
    left: 0; right: 0; top: 120px;
    display: flex; justify-content: center; align-items: center; gap: 18px;
  }
  .brand-dot {
    flex: none;
    width: 34px; height: 34px; border-radius: 50%;
    background: var(--ink);
  }
  .brand-name {
    font-weight: 700;
    font-size: 54px;
    letter-spacing: 1px;
    color: var(--ink);
    text-transform: uppercase;
    white-space: nowrap;
  }
  .card-front .band {
    position: absolute; left: 0; right: 0; bottom: 0; height: 150px;
    background: linear-gradient(180deg, var(--card-dark-2), var(--card-dark));
  }
  .card-front .website {
    position: absolute; left: 230px; bottom: 42px;
    color: #ffffff; font-weight: 700; font-size: 26px; letter-spacing: 2px;
  }
  .stripes { position: absolute; }
  .card-front .stripes { right: 40px; top: 342px; width: 330px; height: 70px; }

  /* Back */
  .card-back { background: var(--card-dark); }
  .card-back .brand-panel {
    position: absolute; left: 0; top: 0; width: 290px; height: 100%;
    display: flex; align-items: center; justify-content: center; gap: 12px;
  }
  .card-back .brand-dot { background: #ffffff; width: 22px; height: 22px; }
  .card-back .brand-name { color: #ffffff; font-size: 30px; }
  .card-back .info-panel {
    position: absolute; left: 290px; top: 0; right: 0; bottom: 80px;
    background: var(--card-white);
  }
  .rule {
    position: absolute; left: 0; right: 40px; top: 108px;
    height: 3px; background: var(--red);
  }
  .contact {
    position: absolute; right: 40px; top: 58px;
    text-align: right; color: var(--ink);
  }
  .contact .name { font-size: 38px; font-weight: 600; line-height: 1.2; margin-bottom: 14px; }
  .contact .role { font-size: 26px; margin-bottom: 34px; }
  .contact .line { font-size: 26px; line-height: 1.25; white-space: nowrap; }
  .contact .address { margin-top: 22px; }
  .card-back .stripes { right: 40px; bottom: 14px; width: 330px; height: 60px; }
</style>
</head>
<body>

  <section class="card card-front" aria-label="Frente do cartão">
    <div class="brand">
      <span class="brand-dot"></span>
      <span class="brand-name">Rodas Lume</span>
    </div>
    <div class="band"></div>
    <p class="website">www.rodaslume.pt</p>
    <svg class="stripes" viewBox="0 0 330 70" aria-hidden="true">
      <polygon points="0,0 80,0 120,70 40,70" fill="var(--grey-1)"/>
      <polygon points="105,0 165,0 205,70 145,70" fill="var(--grey-2)"/>
      <polygon points="200,0 240,0 280,70 240,70" fill="var(--red)"/>
      <polygon points="258,0 290,0 330,70 298,70" fill="var(--pink)"/>
    </svg>
  </section>

  <section class="card card-back" aria-label="Verso do cartão">
    <div class="brand-panel">
      <span class="brand-dot"></span>
      <span class="brand-name">Rodas Lume</span>
    </div>
    <div class="info-panel">
      <div class="rule"></div>
      <div class="contact">
        <p class="name">Augusto Melro</p>
        <p class="role">Gerente</p>
        <p class="line">253 704 862</p>
        <p class="line">geral@rodaslume.pt</p>
        <p class="line address">Rua da Fonteira N.187</p>
        <p class="line">5120-418 Vale Sereno, Alcova</p>
      </div>
    </div>
    <svg class="stripes" viewBox="0 0 330 60" aria-hidden="true">
      <polygon points="0,0 80,0 115,60 35,60" fill="var(--grey-1)"/>
      <polygon points="105,0 165,0 200,60 140,60" fill="var(--grey-2)"/>
      <polygon points="200,0 240,0 275,60 235,60" fill="var(--red)"/>
      <polygon points="258,0 292,0 327,60 293,60" fill="var(--pink)"/>
    </svg>
  </section>

</body>
</html>
```